Ejuice brand looking for label design.

I own a ejuice brand called "Vorlane Ejuice" I am looking for an label design that i can put on my bootles. I want the design to be "Elegant" and classy, in a sophisticated manner.Please check in on my website www.vorlaneejuice.example for a slight idea on what im thinking.

Target Market(s)

Ejuice users

Font styles to use
Decorative
Script

```html
<!DOCTYPE html>
<html lang="en">
<head>
<meta charset="utf-8">
<title>Vorlane Ejuice – Label Design</title>
<link rel="stylesheet" href="https://fonts.googleapis.com/css2?family=Josefin+Sans:wght@300;400;700&display=swap">
<style>
  :root {
    --frame: #d9d9d9;
    --paper: #ffffff;
    --rule: #e6e6e6;
    --green: #2f5d3d;
    --green-dark: #234a2f;
    --linen: #ebe7da;
    --linen-edge: #dedacb;
    --amber-light: #a8621f;
    --amber-dark: #4a2508;
  }
  * { box-sizing: border-box; margin: 0; padding: 0; }
  html, body { width: 732px; height: 1200px; overflow: hidden; background: var(--paper); }
  body { font-family: "Josefin Sans", Arial, sans-serif; }

  .board {
    position: relative;
    width: 732px;
    height: 1200px;
    border: 4px solid var(--frame);
    background: var(--paper);
  }

  .brand-header {
    position: absolute;
    top: 0; left: 0; right: 0;
    height: 328px;
    text-align: center;
    border-bottom: 2px solid var(--rule);
  }
  .brand-name {
    color: var(--green);
    font-weight: 400;
    line-height: 1;
  }
  .brand-header .brand-name {
    padding-top: 56px;
    font-size: 74px;
    letter-spacing: 1px;
  }
  .brand-header .brand-name span { display: block; }
  .brand-header .tagline {
    margin-top: 22px;
    color: var(--green);
    font-size: 34px;
    font-weight: 300;
    letter-spacing: 12px;
    padding-left: 12px;
  }

  .product-shot {
    position: absolute;
    top: 330px; left: 0; right: 0;
    height: 508px;
    display: flex;
    justify-content: center;
    align-items: center;
  }
  .product-shot .bottle {
    width: 200px;
    height: 430px;
    border-radius: 30px 30px 18px 18px;
    background: linear-gradient(90deg, var(--amber-dark), var(--amber-light) 45%, var(--amber-dark));
  }

  .label-panel {
    position: absolute;
    left: 0; right: 0; bottom: 0;
    height: 354px;
    background: radial-gradient(ellipse at center, var(--linen) 55%, var(--linen-edge));
    text-align: center;
  }
  .label-panel .brand-name {
    padding-top: 46px;
    font-size: 56px;
  }
  .label-panel .brand-name span { display: block; }
  .ribbon {
    display: block;
    margin: 8px auto 0;
    width: 300px;
    height: 52px;
  }
  .ribbon text {
    font-family: "Josefin Sans", Arial, sans-serif;
    font-weight: 700;
    font-size: 20px;
    letter-spacing: 3px;
    fill: var(--paper);
  }
  .nicotine-note {
    margin-top: 26px;
    color: var(--green);
    font-size: 15px;
    font-weight: 700;
    letter-spacing: 1px;
  }
  .strength {
    display: inline-block;
    margin-top: 10px;
    padding: 6px 12px 3px;
    border-radius: 14px;
    background: var(--green);
    color: var(--paper);
    font-size: 15px;
    font-weight: 700;
  }
</style>
</head>
<body>
  <main class="board">
    <header class="brand-header">
      <h1 class="brand-name"><span>Vorlane</span><span>Ejuice</span></h1>
      <p class="tagline">FLAVOR</p>
    </header>

    <section class="product-shot">
      <div class="bottle" role="img" aria-label="Photo of an amber dropper bottle wearing the Vorlane Ejuice label"></div>
    </section>

    <section class="label-panel">
      <h2 class="brand-name"><span>Vorlane</span><span>Ejuice</span></h2>
      <svg class="ribbon" viewBox="0 0 300 52" aria-label="Type flavor">
        <polygon points="0,12 36,12 36,50 0,50 12,31" fill="var(--green-dark)"/>
        <polygon points="300,12 264,12 264,50 300,50 288,31" fill="var(--green-dark)"/>
        <rect x="24" y="4" width="252" height="38" fill="var(--green)"/>
        <text x="150" y="30" text-anchor="middle">TYPE FLAVOR</text>
      </svg>
      <p class="nicotine-note">CONTAINS NICOTINE</p>
      <p class="strength">2%</p>
    </section>
  </main>
</body>
</html>
```